Dyrano In-home Personal Training

I would like to have some eye-catching business card design. Opened to any ideas.

The business idea: mobile fitness - train clients at their places

Target Market(s)

General population, 20-60 years old

Industry/Entity Type

Fitness

Contact Information for Business Card

The information to include:
Name: Marta
Call or text: 306-555-0187
Website: Dyrano.ca
Please use the attached logo

Requirements
Should not have
• No orange or purple colours please

```html
<!DOCTYPE html>
<html lang="en">
<head>
<meta charset="utf-8">
<title>Dyrano In-home Personal Training — Business Card</title>
<link href="https://fonts.googleapis.com/css2?family=Titillium+Web:wght@300;400;600&display=swap" rel="stylesheet">
<style>
  :root {
    --backdrop: #e7e4df;
    --card: #3a3b3e;
    --card-edge: #2f3033;
    --band-dark: #202123;
    --band-soft: #2c2d30;
    --text-light: #f2f2f2;
    --text-emboss: #27282a;
  }
  html, body {
    margin: 0;
    width: 1200px;
    height: 859px;
    overflow: hidden;
    background: var(--backdrop);
    font-family: "Titillium Web", sans-serif;
  }
  .canvas {
    position: relative;
    width: 1200px;
    height: 859px;
  }
  .card {
    position: absolute;
    top: 289px;
    width: 501px;
    height: 286px;
    background: linear-gradient(160deg, #424347 0%, var(--card) 55%, var(--card-edge) 100%);
    overflow: hidden;
  }
  .card--front { left: 59px; }
  .card--back { left: 639px; }
  .card__bands {
    position: absolute;
    inset: 0;
    width: 100%;
    height: 100%;
  }
  .band--dark { fill: var(--band-dark); }
  .band--soft { fill: var(--band-soft); }

  .brand {
    position: absolute;
    left: 26px;
    top: 26px;
    margin: 0;
    color: var(--text-light);
    font-weight: 300;
    font-size: 34px;
    letter-spacing: 4px;
    line-height: 1;
  }
  .holder {
    position: absolute;
    left: 25px;
    top: 128px;
    margin: 0;
    color: var(--text-light);
    font-weight: 400;
    font-size: 31px;
    line-height: 1;
  }
  .holder__marker {
    position: absolute;
    left: 1px;
    top: 134px;
    width: 4px;
    height: 25px;
    background: var(--text-light);
  }
  .contact {
    position: absolute;
    left: 26px;
    top: 213px;
    margin: 0;
    color: var(--text-light);
    font-size: 14.5px;
    line-height: 18px;
    font-weight: 400;
  }
  .contact strong { font-weight: 600; }

  .brand--emboss {
    left: 293px;
    top: 128px;
    color: var(--text-emboss);
    font-size: 38px;
    letter-spacing: 6px;
  }
</style>
</head>
<body>
<main class="canvas">
  <section class="card card--front" aria-label="Card front">
    <svg class="card__bands" viewBox="0 0 700 400" preserveAspectRatio="none" aria-hidden="true">
      <polygon class="band--dark" points="700,100 700,185 485,400 400,400"/>
      <polygon class="band--soft" points="700,210 700,255 555,400 510,400"/>
    </svg>
    <p class="brand">Dyrano</p>
    <span class="holder__marker"></span>
    <h1 class="holder">Marta</h1>
    <p class="contact">Call or text: 306-555-0187<br>Website: www.<strong>Dyrano</strong>.ca</p>
  </section>

  <section class="card card--back" aria-label="Card back">
    <svg class="card__bands" viewBox="0 0 700 400" preserveAspectRatio="none" aria-hidden="true">
      <polygon class="band--soft" points="55,0 90,0 0,90 0,55"/>
      <polygon class="band--dark" points="100,0 200,0 0,200 0,100"/>
    </svg>
    <p class="brand brand--emboss">Dyrano</p>
  </section>
</main>
</body>
</html>
```